"Harbor Constructors" is a residential building company and needs a new business card design and may re

We would like a redesign based on the existing logo, and would like to see a new font as well. We are bespoke home builders who build sustainable energy efficient homes.

Industry/Entity Type

Construction

Contact Information for Business Card

Business card size 40mm x 90mm

Colors

Designer to choose colors to be used in the design.

```html
<!DOCTYPE html>
<html lang="en">
<head>
<meta charset="utf-8">
<title>Harbor Constructors – Business Card</title>
<link rel="stylesheet" href="https://fonts.googleapis.com/css2?family=Montserrat:wght@500;600&family=Open+Sans:wght@400;600&display=swap">
<style>
  :root {
    --backdrop: #0c0c0c;
    --card-light: #ffffff;
    --card-dark: #161616;
    --accent: #a8c62b;
    --ink-dark: #1b1b1b;
    --ink-light: #f2f2f2;
    --ink-muted: #cfcfcf;
  }
  * { box-sizing: border-box; margin: 0; padding: 0; }
  html, body {
    width: 1200px; height: 1000px; overflow: hidden;
    background: var(--backdrop);
  }
  .stage {
    position: relative; width: 1200px; height: 1000px;
  }
  .card {
    position: absolute; left: 240px; width: 720px; height: 320px;
    border-radius: 3px;
    box-shadow: 0 18px 40px rgba(0,0,0,.6);
  }
  .card--front { top: 110px; background: var(--card-light); }
  .card--back {
    top: 570px;
    background: linear-gradient(135deg, #1c1c1c 0%, var(--card-dark) 60%, #121212 100%);
    font-family: "Open Sans", sans-serif;
    color: var(--ink-muted);
  }

  /* Front: brand lockup */
  .brand {
    position: absolute; left: 50%; top: 50%;
    transform: translate(-50%, -50%);
    display: flex; align-items: center; gap: 12px;
  }
  .brand__mark {
    width: 18px; height: 18px; background: var(--accent);
  }
  .brand__name {
    font-family: "Montserrat", sans-serif; font-weight: 500;
    font-size: 26px; letter-spacing: 1px; color: var(--ink-dark);
  }

  /* Back: details */
  .person { position: absolute; left: 60px; top: 44px; }
  .person__name {
    font-family: "Montserrat", sans-serif; font-weight: 600;
    font-size: 26px; color: var(--ink-light); letter-spacing: .3px;
  }
  .person__name .surname { color: var(--accent); }
  .person__reg { font-size: 13.5px; margin-top: 4px; color: var(--ink-muted); }

  .company {
    position: absolute; left: 60px; top: 128px;
    font-family: "Montserrat", sans-serif; font-weight: 600;
    font-size: 15px; color: var(--accent);
  }
  .contacts {
    position: absolute; left: 60px; top: 162px;
    list-style: none; font-size: 14px; line-height: 24px;
  }
  .contacts li { display: flex; align-items: center; gap: 10px; }
  .contacts svg { width: 13px; height: 13px; fill: var(--accent); flex: none; }

  .back-mark {
    position: absolute; right: 70px; top: 110px;
    width: 70px; height: 70px; background: var(--accent);
  }
  .address {
    position: absolute; right: 56px; bottom: 36px;
    text-align: right; font-size: 14.5px; line-height: 21px;
    color: var(--ink-light); font-style: normal;
  }
</style>
</head>
<body>
<main class="stage">
  <section class="card card--front" aria-label="Card front">
    <div class="brand">
      <span class="brand__mark"></span>
      <span class="brand__name">harbor constructors</span>
    </div>
  </section>

  <section class="card card--back" aria-label="Card back">
    <div class="person">
      <h1 class="person__name">Daniel <span class="surname">Corvetti</span></h1>
      <p class="person__reg">Registration 40518 ABN: 12 345 678 901</p>
    </div>
    <p class="company">Harbor Constructors Pty Ltd</p>
    <ul class="contacts">
      <li>
        <svg viewBox="0 0 24 24" aria-hidden="true"><path d="M6.6 10.8a15.1 15.1 0 0 0 6.6 6.6l2.2-2.2c.3-.3.7-.4 1-.2 1.1.4 2.3.6 3.6.6.6 0 1 .4 1 1V20c0 .6-.4 1-1 1A17 17 0 0 1 3 4c0-.6.4-1 1-1h3.5c.6 0 1 .4 1 1 0 1.3.2 2.5.6 3.6.1.3 0 .7-.2 1z"/></svg>
        0400 555 017
      </li>
      <li>
        <svg viewBox="0 0 24 24" aria-hidden="true"><path d="M2 5h20v14H2zm2 2v.5l8 5 8-5V7z"/></svg>
        daniel@harborconstructors.com.au
      </li>
      <li>
        <svg viewBox="0 0 24 24" aria-hidden="true"><path d="M12 2a10 10 0 1 0 0 20 10 10 0 0 0 0-20zm7.9 9h-3.4a15 15 0 0 0-1.3-6A8 8 0 0 1 19.9 11zM12 4c.9 1.2 2 3.6 2.4 7H9.6C10 7.6 11.1 5.2 12 4zM8.8 5a15 15 0 0 0-1.3 6H4.1A8 8 0 0 1 8.8 5zM4.1 13h3.4a15 15 0 0 0 1.3 6A8 8 0 0 1 4.1 13zM12 20c-.9-1.2-2-3.6-2.4-7h4.8c-.4 3.4-1.5 5.8-2.4 7zm3.2-1a15 15 0 0 0 1.3-6h3.4a8 8 0 0 1-4.7 6z"/></svg>
        www.harborconstructors.com.au
      </li>
    </ul>
    <span class="back-mark" aria-hidden="true"></span>
    <address class="address">
      PO Box 2140<br>
      Lakeside LPO<br>
      Bayview, WA 6999
    </address>
  </section>
</main>
</body>
</html>
```